Modern Business Card For A Digital Advertising Company

I'll be print on the Tarn Prints Velour paper http://us.tarnprints.example/products/velour/business-cards.html
Need's to be modern and use the color palette of the logo or gray scales. I think integrating the pixelation of the logo in to the card and having it wrap from one side to the other could be interesting. My company provides ad operations, web development, and number of other services to websites around the world. You can see my website at http://www.pixelharbor.example
Contact info on the card needs to have
Dana Welloby
President
p.555.318.4406
dana@pixelharbor.example
http://www.pixelharbor.example
Doesn't necessarily need to be in that order
Target Market(s)
Website owners
Industry/Entity Type
Business
Look and feel

```html
<!DOCTYPE html>
<html lang="en">
<head>
<meta charset="utf-8">
<title>Pixel Harbor – Business Card</title>
<link href="https://fonts.googleapis.com/css2?family=Open+Sans:wght@400;700&display=swap" rel="stylesheet">
<style>
  :root {
    --backdrop: #5b5b5b;
    --card: #ffffff;
    --green: #8dc43f;
    --icon-green: #3aa047;
    --ink: #4a4a48;
    --text: #222222;
    --band: #000000;
  }
  * { margin: 0; padding: 0; box-sizing: border-box; }
  html, body { width: 983px; height: 1200px; overflow: hidden; }
  body {
    background: var(--backdrop);
    position: relative;
    font-family: "Open Sans", Arial, sans-serif;
  }
  .card {
    position: absolute;
    left: 62px;
    width: 867px;
    height: 494px;
    background: var(--card);
    border-radius: 28px;
    overflow: hidden;
  }
  .card-front { top: 63px; }
  .card-back { top: 638px; }
  .swoosh { position: absolute; inset: 0; width: 100%; height: 100%; }

  .brand {
    position: absolute;
    display: flex;
    align-items: center;
    gap: 16px;
    color: var(--green);
    font-weight: 700;
    letter-spacing: 2px;
    white-space: nowrap;
  }
  .brand-mark { background: var(--green); flex: none; }
  .card-front .brand {
    left: 0; right: 0; top: 160px;
    justify-content: center;
    font-size: 46px;
  }
  .card-front .brand-mark { width: 56px; height: 56px; }
  .card-back .brand {
    left: 50px; top: 120px;
    font-size: 34px;
  }
  .card-back .brand-mark { width: 42px; height: 42px; }

  .role {
    position: absolute; left: 52px; top: 264px;
    font-size: 24px; color: var(--text);
  }
  .person {
    position: absolute; left: 50px; top: 296px;
    font-size: 32px; font-weight: 700; color: var(--ink);
  }
  .divider {
    position: absolute; left: 500px; top: 102px;
    width: 2px; height: 195px; background: #333;
  }
  .contact-list {
    position: absolute; left: 514px; top: 162px;
    list-style: none;
  }
  .contact-list li {
    display: flex; align-items: center; gap: 8px;
    height: 40px;
    font-size: 22px; color: var(--text);
    white-space: nowrap;
  }
  .contact-list svg { width: 24px; height: 24px; flex: none; }
</style>
</head>
<body>

<section class="card card-front">
  <div class="brand"><span class="brand-mark"></span>PIXEL HARBOR</div>
  <svg class="swoosh" viewBox="0 0 867 494" preserveAspectRatio="none" aria-hidden="true">
    <path fill="var(--band)" d="M0 298 C 300 325, 580 430, 867 440 L867 494 L0 494 Z"/>
    <path fill="var(--green)" d="M0 309 C 300 345, 560 465, 867 476 L867 494 L0 494 Z"/>
  </svg>
</section>

<section class="card card-back">
  <svg class="swoosh" viewBox="0 0 867 494" preserveAspectRatio="none" aria-hidden="true">
    <path fill="var(--band)" d="M0 441 C 300 425, 560 320, 867 297 L867 494 L0 494 Z"/>
    <path fill="var(--green)" d="M0 476 C 300 455, 560 345, 867 297 L867 494 L0 494 Z"/>
  </svg>
  <div class="brand"><span class="brand-mark"></span>PIXEL HARBOR</div>
  <p class="role">President</p>
  <p class="person">Dana Welloby</p>
  <div class="divider"></div>
  <ul class="contact-list">
    <li>
      <svg viewBox="0 0 24 24" aria-hidden="true"><circle cx="12" cy="12" r="10" fill="none" stroke="var(--icon-green)" stroke-width="1.6"/><path d="M9 6.5c-1.5.8-2 2.5-1 4.6 1.1 2.4 2.8 4.3 5 5.6 1.6.9 3 .6 3.8-.6l-1.8-1.6-1.3.8c-1.3-.7-2.6-2.2-3.3-3.6l1-1.2L9 6.5z" fill="var(--icon-green)"/></svg>
      555-318-4406
    </li>
    <li>
      <svg viewBox="0 0 24 24" aria-hidden="true"><rect x="2.5" y="6" width="19" height="13" fill="none" stroke="var(--icon-green)" stroke-width="1.6"/><path d="M2.5 6l9.5 7 9.5-7M2.5 19l7-6M21.5 19l-7-6" fill="none" stroke="var(--icon-green)" stroke-width="1.4"/></svg>
      dana@pixelharbor.example
    </li>
    <li>
      <svg viewBox="0 0 24 24" aria-hidden="true"><g fill="none" stroke="var(--icon-green)" stroke-width="1.6"><circle cx="12" cy="12" r="9.5"/><ellipse cx="12" cy="12" rx="4" ry="9.5"/><path d="M2.5 12h19M4 7h16M4 17h16"/></g></svg>
      www.pixelharbor.example
    </li>
  </ul>
</section>

</body>
</html>
```